A friend who listens

find a friend who listens. place holder site:

http://afriendwholistens-example.com/

Coding

Coded - Design and coding required

Number of Pages Required

5+ page

Colors

Designer to choose colors to be used in the design.

```html
<!DOCTYPE html>
<html lang="en">
<head>
<meta charset="utf-8">
<title>A friend who listens – Listener Login</title>
<link href="https://fonts.googleapis.com/css2?family=Roboto:wght@300;400;500;700;900&display=swap" rel="stylesheet">
<style>
:root{
  --backdrop:#e6e6e6;
  --white:#ffffff;
  --yellow:#ffbb40;
  --teal:#00967a;
  --red:#e8381e;
  --orange:#ea4e1c;
  --purple:#540573;
  --purple-dark:#44045f;
  --purple-soft:#6d1f6e;
  --purple-light:#7b3a94;
  --plum:#5c2483;
  --green:#22a50a;
  --ink:#222222;
  --gold:#ffd21f;
}
*{margin:0;padding:0;box-sizing:border-box}
html,body{width:1200px;height:1200px;overflow:hidden;background:var(--backdrop);font-family:'Roboto',sans-serif}
.page{position:absolute;left:204px;top:0;width:798px;height:1200px;background:var(--white);overflow:hidden}
.abs{position:absolute}
.shape{position:absolute;left:0;top:0}

/* header */
.brand{position:absolute;left:27px;top:12px;display:flex;align-items:center;gap:6px}
.brand-dot{width:36px;height:36px;border-radius:50%;background:var(--orange)}
.brand-name{font-size:13px;font-weight:700;color:var(--plum);line-height:1.05;width:80px}
.nav{position:absolute;top:18px;left:433px;display:flex;align-items:center;font-size:6px;font-weight:700;color:var(--white);letter-spacing:.1px}
.nav span{margin-right:19px}
.nav .active{color:var(--orange)}
.nav .create{background:var(--orange);border-radius:8px;padding:3px 7px;margin-right:12px}
.menu-icon{width:12px;height:8px;border-top:1.5px solid #fff;border-bottom:1.5px solid #fff;position:relative}
.menu-icon::after{content:"";position:absolute;left:0;right:0;top:2px;border-top:1.5px solid #fff}

.hero-title{position:absolute;left:167px;top:76px;font-size:21.5px;font-weight:900;color:var(--teal);line-height:25px}
.hero-text{position:absolute;left:167px;top:142px;width:210px;font-size:10px;line-height:20.7px;color:var(--red)}
.btn-details{position:absolute;left:166px;top:220px;width:96px;height:25px;border-radius:13px;background:var(--plum);color:var(--gold);font-size:7.5px;font-weight:500;display:flex;align-items:center;justify-content:center}
.hero-art{position:absolute;left:409px;top:52px;width:285px;height:285px;border-radius:48% 52% 50% 50%;background:linear-gradient(150deg,#8fd9ee,#a5e0f4 60%,#7e73e8)}

.login-title{position:absolute;left:0;width:798px;top:414px;text-align:center;font-size:20px;font-weight:300;color:var(--orange)}
.login-title b{font-weight:700}

/* purple section */
.dashboard{position:absolute;left:0;top:465px;width:798px;height:388px;background:var(--purple);overflow:hidden}
.tabs{position:absolute;top:22px;left:0;width:798px;display:flex;justify-content:center;gap:11px;font-size:12.5px}
.tab{padding:0 2px 4px;color:var(--orange);border-bottom:2px solid var(--orange)}
.tab.current{color:var(--white);border-color:var(--white)}
.pill{position:absolute;top:68px;width:131px;height:29px;border-radius:15px;color:#fff;display:flex;align-items:center;justify-content:center;font-weight:500}
.timer{left:158px;background:var(--orange);font-size:15px}
.available{left:303px;background:var(--green);font-size:12.5px}
.listener{position:absolute;left:157px;width:485px;height:60px;background:var(--purple-dark)}
.photo{position:absolute;left:10px;top:7px;width:47px;height:46px;background:linear-gradient(160deg,#3fc3cf,#b72c2e)}
.name{position:absolute;left:78px;top:8px;font-size:10px;font-weight:500;color:#fff}
.stars{position:absolute;left:145px;top:9px;font-size:8px;letter-spacing:.3px;color:var(--gold)}
.stars i{font-style:normal;color:#bdb7c7}
.meta{position:absolute;left:78px;top:24px;font-size:7.3px;line-height:13.3px;color:#fff}
.btn-listen{position:absolute;left:365px;top:18px;width:106px;height:23px;border-radius:12px;background:var(--orange);color:#fff;font-size:10px;font-weight:500;display:flex;align-items:center;justify-content:center}
.pager{position:absolute;top:338px;left:364px;display:flex;align-items:center;gap:6px;font-size:10px;font-weight:500;color:#fff}
.pager .on{background:var(--orange);padding:2px 6px}

/* benefits */
.benefits{position:absolute;left:0;top:853px;width:798px;height:347px;background:linear-gradient(100deg,#e8451d 0%,#ea561f 45%,#f59a35 80%,#fbb33d 100%);overflow:hidden}
.benefits-title{position:absolute;top:50px;left:0;width:798px;text-align:center;font-size:20px;font-weight:300;color:var(--ink)}
.benefits-title b{font-weight:700}
.icon-box{position:absolute;width:35px;height:35px;border:1px solid #fff;display:flex;align-items:center;justify-content:center}
.benefit{position:absolute;top:180px;width:190px;text-align:center}
.benefit h3{font-size:9.5px;font-weight:700;color:var(--ink);margin-bottom:9px}
.benefit p{font-size:7.4px;line-height:12.4px;color:#fff;font-weight:300}
</style>
</head>
<body>
<div class="page">
  <svg class="shape" width="798" height="465" viewBox="0 0 798 465">
    <path fill="var(--yellow)" d="M0 0 H154 Q185 15 199 45 L166 47 Q172 120 120 155 Q60 185 0 150 Z"/>
    <path fill="var(--teal)" d="M382 0 H798 V255 Q740 330 640 355 Q560 370 470 345 Q410 325 343 288 L417 251 Q375 190 380 110 Q382 50 382 0 Z"/>
  </svg>

  <div class="brand"><div class="brand-dot"></div><div class="brand-name">A friend who listens</div></div>
  <nav class="nav">
    <span>ADMIN</span><span>ABOUT / CONTACT</span><span>HELP</span>
    <span class="active">LISTENER LOGIN ⌄</span><span>USER LOGIN ⌄</span>
    <span class="create">CREATE ACCOUNT</span><div class="menu-icon"></div>
  </nav>

  <h1 class="hero-title">FOR LISTENER USER<br>AT FIRST LOGIN</h1>
  <p class="hero-text">Lorem ipsum dolor sit amet, consectetur adipiscing elit, sed do eiusmod tempor incididunt ut labore et dolore magna aliqua..</p>
  <div class="btn-details">VIEW DETAILS</div>
  <div class="hero-art" role="img" aria-label="Illustration of a listener with headphones walking beside a listener booking card"></div>

  <h2 class="login-title">LISTENER <b>LOGIN</b></h2>

  <section class="dashboard">
    <svg class="shape" width="798" height="388" viewBox="0 0 798 388">
      <path fill="var(--purple-soft)" d="M0 60 Q90 40 170 90 Q220 120 200 200 Q180 290 110 320 Q50 345 0 325 Z"/>
      <path fill="var(--purple-light)" d="M798 0 V187 Q720 190 680 150 Q650 120 635 60 L700 78 Q705 30 745 10 Q770 0 798 0 Z"/>
    </svg>
    <div class="tabs">
      <span class="tab current">Clock in/Set Status as Available</span>
      <span class="tab">Transaction History</span>
      <span class="tab">Payout</span>
    </div>
    <div class="pill timer">12:30:15</div>
    <div class="pill available">Available</div>

    <div class="listener" style="top:120px">
      <div class="photo" role="img" aria-label="Listener profile photo"></div>
      <div class="name">Mara Lind</div><div class="stars">★★★★<i>★</i></div>
      <div class="meta">Radio Artist<br>California, USA</div>
      <div class="btn-listen">LISTEN NOW</div>
    </div>
    <div class="listener" style="top:186px">
      <div class="photo" role="img" aria-label="Listener profile photo"></div>
      <div class="name">Mara Lind</div><div class="stars">★★★★<i>★</i></div>
      <div class="meta">Radio Artist<br>California, USA</div>
      <div class="btn-listen">LISTEN NOW</div>
    </div>
    <div class="listener" style="top:253px">
      <div class="photo" role="img" aria-label="Listener profile photo"></div>
      <div class="name">Mara Lind</div><div class="stars">★★★★<i>★</i></div>
      <div class="meta">Radio Artist<br>California, USA</div>
      <div class="btn-listen">LISTEN NOW</div>
    </div>
    <div class="pager"><span class="on">1</span><span>2</span><span>3</span><span>Next</span></div>
  </section>

  <section class="benefits">
    <svg class="shape" width="798" height="347" viewBox="0 0 798 347">
      <path fill="#f6bb5c" opacity=".7" d="M798 0 V265 Q740 285 690 282 L716 240 Q660 220 640 150 Q625 70 680 25 Q710 0 740 0 Z"/>
      <path fill="#ef8a6a" opacity=".8" d="M0 250 Q60 225 137 250 L103 278 Q130 310 138 347 H0 Z"/>
    </svg>
    <h2 class="benefits-title">BENEFITS OF TALKING <b>TO SOMEONE</b></h2>

    <div class="icon-box" style="left:264px;top:124px">
      <svg width="22" height="22" viewBox="0 0 22 22" fill="none" stroke="#fff" stroke-width="1.3"><circle cx="7" cy="9" r="3" fill="#fff"/><path d="M2 20 Q2 13 7 13 Q12 13 12 20 Z" fill="#fff"/><rect x="11" y="2" width="9" height="6" rx="1"/><path d="M13 8 L12 11 L15 8"/></svg>
    </div>
    <div class="icon-box" style="left:501px;top:124px">
      <svg width="22" height="22" viewBox="0 0 22 22" fill="none" stroke="#fff" stroke-width="2"><path d="M5 3 V18 M2 15 L5 19 L8 15 M10 4 H20 M10 9 H18 M10 14 H15 M10 19 H13"/></svg>
    </div>

    <div class="benefit" style="left:189px">
      <h3>BENEFITS OF TALKING TO SOMEONE</h3>
      <p>If you or someone you know is going through a tough time, talking to someone might sound like a simplistic solution but it really is one of the best possible things you/they can do. Though it can be hard to build up the courage, telling someone you trust how you're feeling can help in loads of ways:</p>
    </div>
    <div class="benefit" style="left:434px">
      <h3>SORTING THROUGH YOUR FEELINGS</h3>
      <p>Talking out loud about what's going on in your head and explaining it to someone else, even if you think it doesn't make sense, helps you to clarify the things that are worrying you.<br>Saying things out loud, often makes them less scary, and at least by having to sort through your feelings</p>
    </div>

    <div class="icon-box" style="left:264px;top:295px">
      <svg width="22" height="22" viewBox="0 0 22 22" fill="none" stroke="#fff" stroke-width="1.2"><path d="M11 2 L19 6 V15 L11 20 L3 15 V6 Z M3 6 L11 10 L19 6 M11 10 V20 M7 4 L15 8 M15 4 L7 8"/></svg>
    </div>
    <div class="icon-box" style="left:505px;top:295px">
      <svg width="22" height="22" viewBox="0 0 22 22" fill="none" stroke="#fff" stroke-width="1.2"><path d="M6 20 V15 Q2 12 3 7 Q5 2 11 2 Q15 2 16 6 L15 12 L12 13 V20"/><path d="M15 6 Q18 3 20 6 Q18 7 17 10"/></svg>
    </div>
  </section>
</div>
</body>
</html>
```